Need Website for PR Firm

I need a website for my new business, Lantern Hill Agency, a PR, Communications and Marketing Firm. I want something classy and clean. Tailored and professional with a bit of a whimsical touch. Colors are mainly white and green. I don't like random stock photos but I would consider an image of a park with the city in the background. The name of my company is a play on Willowmere Green in Brooklyn where I am based.

The navigation and pages I will need is a good clean landing page.
About us
Who we are
Contact

Again, I like clean white and the copy in a similar color and font as my logo.
No stock photography or clip art.
I uploaded an image of the park that I like and wld be open to using in some way
Updates

I have uploaded an image of the park that you could implemented. 

Seeing some good designs here.

With the image I uploaded, I unfortunately think the green sky is too green.
Wondering if we can make modifications to the color of the sky.
I like the last image submitted too.

Target Market(s)

Professionals and the media who are seeing how I represent myself and my agency as they hire me for the public relations council.

Industry/Entity Type

Business

Font styles to use
Serif
Other font styles liked:
• Trajan

Colors
acd036
ffffff
dbdbdb
eeeeee

Requirements
Must have
• High quality and consistent colors and font.
Should not have
• Stock photography
Clip art
colors that aren't white, the green in my font, black or gray if necessary.

```html
<!DOCTYPE html>
<html lang="en">
<head>
<meta charset="utf-8">
<title>Lantern Hill Agency</title>
<link href="https://fonts.googleapis.com/css2?family=Yanone+Kaffeesatz:wght@400&display=swap" rel="stylesheet">
<style>
:root{
  --green:#8aad1a;
  --green-light:#acd036;
  --bg:#f5f5f5;
  --rule:#e4e4e4;
  --band:#e3e3e3;
  --text:#777777;
  --heading:#5a5a5a;
  --nav:#8c8c8c;
  --badge:#a3a3a3;
  --footer:#555555;
  --caption:rgba(45,45,45,.82);
}
*{margin:0;padding:0;box-sizing:border-box}
html,body{width:1005px;height:1200px;overflow:hidden;background:var(--bg)}
body{position:relative;font-family:Arial,Helvetica,sans-serif;font-size:10.5px;line-height:15.6px;color:var(--text)}
.display{font-family:"Yanone Kaffeesatz",sans-serif;font-weight:400}
.abs{position:absolute}
.rule{position:absolute;left:137px;width:730px;height:1px;background:var(--rule)}
.brand{left:137px;top:50px;display:flex;align-items:center;gap:10px}
.brand-mark{width:22px;height:22px;background:var(--green)}
.brand-name{font-family:"Yanone Kaffeesatz",sans-serif;font-size:30px;color:var(--green);letter-spacing:.5px}
.nav{right:138px;top:45px;display:flex;gap:23px;font-size:16px}
.nav a{color:var(--nav);text-decoration:none}
.nav a.active{color:var(--green)}
.slider{left:137px;top:137px;width:730px;height:279px;background:#e0e0e0;border-bottom:15px solid #cfcfcf}
.slider-photo{position:absolute;left:0;top:15px;width:730px;height:249px;
  background:linear-gradient(180deg,#ffffff 0%,#f1f1f1 35%,#c9c4bc 55%,#8fa36a 70%,#557a3a 88%,#6e8a4e 100%)}
.caption{position:absolute;left:16px;top:145px;width:287px;height:104px;background:var(--caption);padding:14px 15px}
.caption h2{font-size:20px;color:#fff;line-height:22px;margin-bottom:7px}
.caption p{color:#d8d8d8;font-size:10.3px}
.arrow{position:absolute;top:352px;width:32px;height:32px}
.band{position:absolute;left:137px;width:730px;height:11px;background:var(--band)}
.welcome{left:137px;top:473px;width:460px}
.welcome h1{font-size:22px;color:var(--heading);line-height:26px;margin-bottom:3px}
.welcome h1 span{color:var(--green)}
.who{left:137px;top:589px;width:170px}
.who h2{font-size:29px;color:#8c8c8c;line-height:30px;margin-bottom:14px}
.who p{font-style:italic;color:#9a9a9a}
.btn{display:inline-block;background:var(--green);color:#fff;font-size:8.5px;line-height:20px;padding:0 6px;font-weight:bold}
.divider{left:309px;top:589px;width:1px;height:120px;background:var(--rule)}
.step{top:589px;width:166px}
.step-head{display:flex;align-items:flex-start;height:17px}
.step .num{width:25px;height:25px;border-radius:50%;background:var(--badge);color:#fff;font-size:11px;line-height:25px;text-align:center;float:left;margin:1px 8px 0 0}
.step h3{font-size:18px;color:var(--green);line-height:20px}
.section-title{font-size:18px;color:var(--green);line-height:20px}
.about{left:137px;top:772px;width:360px}
.about p{margin-bottom:12px}
.contact{left:513px;top:772px;width:330px}
.contact label{display:block;font-size:9.5px;line-height:14px}
.field{width:273px;height:26px;border:1px solid #d8d8d8;background:#f8f8f8;margin-bottom:10px}
.area{width:329px;height:120px;border:1px solid #d8d8d8;background:#f8f8f8;margin-bottom:10px}
.footer{left:0;top:1160px;width:1005px;height:40px;background:var(--footer);color:#e6e6e6;font-size:8px;padding:19px 0 0 137px}
</style>
</head>
<body>
<div class="rule" style="top:24px"></div>
<div class="abs brand"><span class="brand-mark"></span><span class="brand-name">Lantern Hill Agency</span></div>
<nav class="abs nav display"><a class="active" href="#">Home</a><a href="#">About</a><a href="#">Who We Are</a><a href="#">Contact</a></nav>
<div class="rule" style="top:113px"></div>

<div class="abs slider">
  <div class="slider-photo" role="img" aria-label="Park lawn and trees with city skyscrapers in the background"></div>
  <div class="caption">
    <h2 class="display">When Day And Dream Unite</h2>
    <p>Praesent nec aliquet elit. Nullam convallis placerat metus, sit amet ultrices nulla faucibus sit amet. Quisque dictum lorem sed sem pharetra luctus.</p>
  </div>
</div>
<svg class="arrow" style="left:776px" viewBox="0 0 32 32"><circle cx="16" cy="16" r="16" fill="rgba(60,60,60,.55)"/><path d="M18 11l-5 5 5 5" stroke="#fff" stroke-width="2" fill="none"/></svg>
<svg class="arrow" style="left:818px" viewBox="0 0 32 32"><circle cx="16" cy="16" r="16" fill="rgba(60,60,60,.55)"/><path d="M14 11l5 5-5 5" stroke="#fff" stroke-width="2" fill="none"/></svg>

<div class="band" style="top:447px"></div>
<div class="abs welcome">
  <h1 class="display">Welcome to <span>Lantern Hill Marketing</span></h1>
  <p>Lorem ipsum dolor sit amet, consectetur adipiscing elit. Duis nec purus tellus, quis pulvinar tortor. Sed mattis lobortis gravida. Integer convallis ipsum in neque tempus posuere.</p>
</div>
<div class="band" style="top:548px"></div>

<div class="abs who">
  <h2 class="display">WHO WE ARE</h2>
  <p>Lorem ipsum dolor sit amet, consec adipiscing elit. Duis nec purus.</p>
  <a class="btn" href="#" style="margin-top:16px">Read More</a>
</div>
<div class="abs divider"></div>
<div class="abs step" style="left:326px"><span class="num">1</span><h3 class="display">Business Consulting</h3><p>Lorem ipsum dolor sit amet, consecadipiscing elit. Duis nec purus tellus, quis pulvinar tortor. Sed mattis loborti gravida. Integer convallis.</p></div>
<div class="abs step" style="left:514px"><span class="num">2</span><h3 class="display">Strategic Planning</h3><p>Lorem ipsum dolor sit amet, consecadipiscing elit. Duis nec purus tellus, quis pulvinar tortor. Sed mattis loborti gravida. Integer convallis.</p></div>
<div class="abs step" style="left:702px"><span class="num">3</span><h3 class="display">Objective Listening</h3><p>Lorem ipsum dolor sit amet, consecadipiscing elit. Duis nec purus tellus, quis pulvinar tortor. Sed mattis loborti gravida. Integer convallis.</p></div>

<div class="band" style="top:730px"></div>

<section class="abs about">
  <h2 class="section-title display">About Us</h2>
  <p>Fusce scelerisque pellentesque mi. Suspendisse elementum tellus ut quam pharetra vel volutpat et, euismod eu sem. Aliquam eget lacus magna quis.</p>
  <p>Fusce scelerisque pellentesque mi. Suspendisse elementum tellus ut quam pharetra vel volutpat et, euismod eu sem. Aliquam eget lacus magna quis.</p>
  <p>Fusce scelerisque pellentesque mi. Suspendisse elementum tellus ut quam pharetra vel volutpat et, euismod eu sem. Aliquam eget lacus magna quis.</p>
  <p>Fusce scelerisque pellentesque mi. Suspendisse elementum tellus ut quam pharetra vel volutpat et, euismod eu sem. Aliquam eget lacus magna quis.</p>
  <p>Fusce scelerisque pellentesque mi. Suspendisse elementum tellus ut quam pharetra vel volutpat et, euismod eu sem. Aliquam eget lacus magna quis.</p>
  <p>Lorem ipsum dolor sit amet, consec adipiscing elit. Duis nec purus mattis lobortis gravida. Aliquam eget lacus magna, quis posuere tellus. Fusce scelerisque pellentesque mi. Suspendisse elementum tellus ut quam pharetra vel volutpat et, euismod eu sem.</p>
  <a class="btn" href="#">Continue Reading</a>
</section>

<section class="abs contact">
  <h2 class="section-title display">Contact Us</h2>
  <label>Name:</label><div class="field"></div>
  <label>E-mail:</label><div class="field"></div>
  <label>Subject:</label><div class="field"></div>
  <label>Message:</label><div class="area"></div>
  <a class="btn" href="#" style="margin-left:2px">Send Message</a>
</section>

<footer class="abs footer">Copyright © 2014 Lantern Hill Marketing. All rights reserved</footer>
</body>
</html>
```